Business card design needed for Automotive Reconditioning business

I have a logo design i just cant decide on the best color or layout for the business card, I will upload all the files so you can see all colors schemes we are considering. I have other file formats if needed let me know.

Target Market(s)

automotive dealerships

Contact Information for Business Card

HERE are the Descriptions and info needed on the card:
Interior Repair: Leather carpet burns panels dash Deoderize
Dealer products and Vin Verify
( spot for name and cell number) My name is Dorian Pelk phone 951 430-2158 Title COO www.BrolvexMotor.com

Font styles to use
Sans Serif
Other font styles liked:
• what ever you think looks best

Requirements
Must have
• Must be able to change the name and phone for employees

```html
<!DOCTYPE html>
<html lang="en">
<head>
<meta charset="utf-8">
<title>Brolvex Motor Reconditioning Corp. — Business Cards</title>
<link rel="stylesheet" href="https://fonts.googleapis.com/css2?family=Exo+2:wght@400;500;600;700&family=Michroma&display=swap">
<style>
  :root {
    --bg: #ebeceb;
    --card: #1e1c1d;
    --green: #8cc63f;
    --white: #ffffff;
    --soft: #e9e9e9;
  }
  * { margin: 0; padding: 0; box-sizing: border-box; }
  html, body { width: 1200px; height: 1200px; overflow: hidden; background: var(--bg); }
  body { position: relative; font-family: "Exo 2", sans-serif; color: var(--white); }

  .card { position: absolute; background: var(--card); overflow: hidden; }
  .card--landscape { left: 74px; top: 265px; width: 643px; height: 357px; }
  .card--portrait { left: 773px; top: 223px; width: 357px; height: 643px; }

  .brand { position: absolute; left: 0; right: 0; text-align: center; font-family: "Exo 2", sans-serif; font-weight: 700; color: var(--white); }
  .brand__name { display: block; letter-spacing: 1px; line-height: 1; }
  .brand__tag { display: block; letter-spacing: 0.5px; margin-top: 8px; line-height: 1; }
  .card--landscape .brand { top: 68px; }
  .card--landscape .brand__name { font-size: 36px; }
  .card--landscape .brand__tag { font-size: 12px; }
  .card--portrait .brand { top: 112px; }
  .card--portrait .brand__name { font-size: 38px; }
  .card--portrait .brand__tag { font-size: 12.5px; }

  .heading { font-family: "Michroma", sans-serif; font-weight: 400; color: var(--white); letter-spacing: -0.5px; white-space: nowrap; }

  .rule { position: absolute; height: 6px; border-top: 1.5px solid var(--white); border-bottom: 1.5px solid var(--green); }
  .rule--left { left: 0; width: 167px; top: 164px; }
  .rule--right { right: 0; width: 167px; top: 164px; }
  .rule--full { left: 0; right: 0; top: 257px; }

  .card--landscape .heading { position: absolute; left: 0; right: 0; top: 155px; text-align: center; font-size: 21px; }

  .services { position: absolute; left: 0; right: 0; top: 192px; text-align: center; color: var(--green); font-weight: 500; font-size: 22px; line-height: 27px; word-spacing: 3px; }

  .contact__name { position: absolute; left: 58px; top: 288px; font-weight: 600; font-size: 22px; }
  .contact__meta { position: absolute; left: 58px; top: 316px; font-size: 16px; }
  .contact__phone { position: absolute; right: 58px; top: 313px; font-size: 20px; letter-spacing: 0.5px; }

  .tab { position: absolute; left: 99px; width: 159px; height: 34px; background: var(--green); }
  .tab--top { top: 0; }
  .tab--bottom { bottom: 0; }

  .card--portrait .heading { position: absolute; left: 0; right: 0; top: 238px; text-align: center; font-size: 24px; }

  .service-list { position: absolute; left: 55px; top: 281px; list-style: none; color: var(--green); font-size: 27px; line-height: 30px; word-spacing: 3px; }
  .service-list li { position: relative; padding-left: 19px; margin-bottom: 12px; }
  .service-list li::before { content: ""; position: absolute; left: 0; top: 12px; width: 7px; height: 7px; background: var(--green); }
  .service-list li.plain { margin-bottom: 0; }
  .service-list li.plain::before { display: none; }
  .service-list li.tight { margin-bottom: 0; }

  .stack { position: absolute; left: 0; right: 0; text-align: center; }
  .stack__name { top: 492px; font-weight: 600; font-size: 31px; }
  .stack__phone { top: 535px; font-size: 20px; letter-spacing: 0.5px; }
  .stack__meta { top: 562px; font-size: 18px; }
</style>
</head>
<body>

<section class="card card--landscape" aria-label="Business card, landscape">
  <div class="brand">
    <span class="brand__name">BROLVEX</span>
    <span class="brand__tag">MOTOR RECONDITIONING CORP.</span>
  </div>
  <div class="rule rule--left"></div>
  <h2 class="heading">REPAIR INTERIOR</h2>
  <div class="rule rule--right"></div>
  <p class="services">Leather carpets, dashboard, instrument panel<br>Deoderize Dealer the Vin and Verify</p>
  <div class="rule rule--full"></div>
  <p class="contact__name">Dorian Pelk</p>
  <p class="contact__meta">COO&nbsp; www.BrolvexMotor.com</p>
  <p class="contact__phone">951 430-2158</p>
</section>

<section class="card card--portrait" aria-label="Business card, portrait">
  <div class="tab tab--top"></div>
  <div class="brand">
    <span class="brand__name">BROLVEX</span>
    <span class="brand__tag">MOTOR RECONDITIONING CORP.</span>
  </div>
  <h2 class="heading">REPAIR INTERIOR</h2>
  <ul class="service-list">
    <li>Leather carpets</li>
    <li>Dashboard</li>
    <li class="tight">Instrument panel</li>
    <li class="plain">Deoderize Dealer</li>
    <li class="plain">the Vin and Verify</li>
  </ul>
  <p class="stack stack__name">Dorian Pelk</p>
  <p class="stack stack__phone">951 430-2158</p>
  <p class="stack stack__meta">COO&nbsp; www.BrolvexMotor.com</p>
  <div class="tab tab--bottom"></div>
</section>

</body>
</html>
```